Lantern of the Meadow website design

To create 2 pages (a front page and sub page) for a health/spiritual website. I have a logo, and was thinking of incorporating Greek temple columns in the design or something similar, but open to other ideas.

The design should suit mobile devices with limited screen space also.

Industry/Entity Type

Health

Number of Pages Required

1 page

```html
<!DOCTYPE html>
<html lang="en">
<head>
<meta charset="utf-8">
<title>Lantern of the Meadow</title>
<link rel="stylesheet" href="https://fonts.googleapis.com/css2?family=Cinzel:wght@400;700&family=Open+Sans:wght@400;600;700&display=swap">
<style>
:root{
  --ink:#222;
  --text:#555;
  --muted:#777;
  --white:#fff;
  --band:#f3f3f3;
  --footer:#2b2b2b;
  --footer-text:#e6e6e6;
  --btn-top:#f2f2f2;
  --btn-bottom:#dcdcdc;
  --sky-top:#1f4a7a;
  --sky-mid:#5d86ad;
  --sea:#0f1e2c;
}
*{box-sizing:border-box;margin:0;padding:0}
html,body{width:1200px;height:2961px;overflow:hidden;background:var(--white)}
body{font-family:"Open Sans",Arial,sans-serif;color:var(--text);position:relative}
section,header,footer{position:absolute;left:0;width:1200px}
.abs{position:absolute}

/* Hero */
.hero{top:0;height:662px}
.hero-bg{left:0;top:0;width:1200px;height:662px;background:linear-gradient(180deg,var(--sky-top) 0%,var(--sky-mid) 48%,#8aa6bf 58%,#2c4560 66%,var(--sea) 100%)}
.brand{left:60px;top:30px;width:200px;text-align:center;color:var(--white)}
.brand .mark{width:56px;height:56px;border-radius:50%;border:3px solid #d8dde3;margin:0 auto 12px}
.brand .name{font-family:"Cinzel",Georgia,serif;font-size:13px;line-height:1.1;white-space:nowrap}
.contact{right:75px;top:38px;color:var(--white);font-size:14px;font-weight:600;display:flex;gap:22px;align-items:center}
.contact span{display:flex;align-items:center;gap:8px}
.nav{right:75px;top:116px;display:flex;gap:40px;font-family:"Cinzel",Georgia,serif;font-size:14px;color:var(--white)}
.nav .active{border-bottom:2px solid var(--white);padding-bottom:6px}
.dropdown{left:578px;top:166px;font-family:"Cinzel",Georgia,serif;font-size:13px;color:var(--white);line-height:27px}
.hero-title{left:75px;top:300px;font-family:"Cinzel",Georgia,serif;font-size:40px;line-height:48px;color:var(--white);letter-spacing:1px;font-weight:400}
.dots{display:flex;gap:8px}
.dots i{width:11px;height:11px;border-radius:50%;background:rgba(255,255,255,.55)}
.dots i:first-child{background:var(--white)}
.hero .dots{left:75px;top:598px}

/* Common */
.heading{font-family:"Cinzel",Georgia,serif;font-size:26px;color:var(--ink);letter-spacing:1px;text-align:center;font-weight:400}
.orn{width:22px;height:22px;border-radius:50%;border:2px solid #888;margin:0 auto 14px}
.btn{display:inline-block;font-family:"Cinzel",Georgia,serif;font-size:14px;color:var(--ink);background:linear-gradient(var(--btn-top),var(--btn-bottom));padding:12px 26px;border:1px solid #d0d0d0}
.para{font-size:14px;line-height:28px;text-align:center}
.photo{position:absolute}

/* Welcome */
.welcome{top:662px;height:358px}
.welcome .inner{position:absolute;left:60px;top:38px;width:1080px;text-align:center}
.welcome .para{margin:20px 0 26px;font-size:13.5px;white-space:nowrap}

/* Offer */
.offer{top:1020px;height:637px;background:var(--band)}
.offer .title{position:absolute;left:0;top:38px;width:1200px}
.card{position:absolute;top:137px;width:330px;text-align:center}
.card .photo{position:relative;height:205px;display:block}
.card h3{font-family:"Cinzel",Georgia,serif;font-size:19px;color:var(--ink);margin:32px 0 8px;letter-spacing:1px}
.card p{font-size:14px;line-height:26px;color:#333;white-space:nowrap}
.arrow{top:230px}

/* Temple */
.temple{top:1657px;height:408px}
.temple .text{left:612px;top:40px;width:512px;text-align:center}
.temple .para{margin:18px 0 26px}

/* Blog & testimonials */
.stories{top:2065px;height:457px;background:var(--band)}
.sub{font-family:"Cinzel",Georgia,serif;font-size:26px;color:var(--ink);letter-spacing:1px;font-weight:400}
.post{top:102px;width:242px}
.post .photo{position:relative;height:155px;display:block}
.post h4{font-family:"Cinzel",Georgia,serif;font-size:16px;color:var(--ink);margin:22px 0 6px;font-weight:700}
.post p{font-size:14px;line-height:22px;color:var(--muted)}
.post .date{font-size:12px;font-weight:700;color:#444;margin-top:10px}
.quote-box{left:614px;top:102px;width:511px;height:213px;background:var(--white);padding:18px 52px;text-align:center}
.quote-box p{font-size:13.5px;line-height:27px;font-style:italic;color:#555}
.quote-box .who{font-size:14px;font-weight:700;color:#333;margin-top:6px}
.qmark{font-family:Georgia,serif;font-size:90px;color:#e6e6e6;line-height:1}
.avatar{left:823px;top:270px;width:92px;height:92px;border-radius:50%;border:4px solid var(--white);background:radial-gradient(circle at 50% 45%,#c9a48a,#6b4a3a)}
.stories .dots{left:836px;top:388px}
.stories .dots i{background:#bbb}
.stories .dots i:first-child{background:#777}

/* Newsletter */
.newsletter{top:2522px;height:280px;text-align:center}
.newsletter .inner{position:absolute;left:0;top:40px;width:1200px}
.newsletter .para{margin:18px 0 20px}
.signup{display:flex;justify-content:center;gap:14px}
.signup .field{width:347px;height:47px;border:1px solid #ddd;font-size:13px;color:#888;text-align:left;padding:14px 16px}
.signup .btn{height:47px;padding:14px 30px}

/* Footer */
.site-footer{top:2802px;height:159px;background:var(--footer);color:var(--footer-text)}
.footnav{left:75px;top:36px;display:flex;gap:32px;font-family:"Cinzel",Georgia,serif;font-size:13px}
.legal{left:75px;top:86px;font-size:12px;line-height:22px;color:#bbb}
.follow{left:945px;top:36px;font-family:"Cinzel",Georgia,serif;font-size:13px}
.socials{left:945px;top:66px;display:flex;gap:12px}
.socials i{width:26px;height:26px;background:#ddd;border-radius:3px}
</style>
</head>
<body>

<header class="hero">
  <div class="abs hero-bg" role="img" aria-label="Seascape at dusk under a blue cloudy sky with a person meditating on the water"></div>
  <div class="abs brand">
    <div class="mark"></div>
    <div class="name">Lantern of the Meadow</div>
  </div>
  <div class="abs contact">
    <span><svg width="13" height="13" viewBox="0 0 24 24"><path fill="#fff" d="M6.6 10.8a15 15 0 0 0 6.6 6.6l2.2-2.2a1 1 0 0 1 1-.25 11.4 11.4 0 0 0 3.6.57 1 1 0 0 1 1 1V20a1 1 0 0 1-1 1A17 17 0 0 1 3 4a1 1 0 0 1 1-1h3.5a1 1 0 0 1 1 1c0 1.25.2 2.45.57 3.57a1 1 0 0 1-.25 1z"/></svg>1-800-555-0142</span>
    <span><svg width="14" height="11" viewBox="0 0 24 18"><path fill="#fff" d="M0 0h24v2L12 10 0 2zM0 4l12 8 12-8v14H0z"/></svg>hello@lanternmeadow.com</span>
  </div>
  <nav class="abs nav">
    <span>Home</span><span>About Us</span><span class="active">Services</span><span>Blog</span><span>Testimonials</span><span>News</span><span>Contact Us</span>
  </nav>
  <div class="abs dropdown">
    <div>› Mind</div><div>› Body</div><div>› Spirit</div>
  </div>
  <h1 class="abs hero-title">DUIS ALIQUAM NIBH A DUI<br>IACULIS VIVERRA</h1>
  <div class="abs dots"><i></i><i></i><i></i><i></i></div>
</header>

<section class="welcome">
  <div class="inner">
    <div class="orn"></div>
    <h2 class="heading">WELCOME TO OUR WEBSITE</h2>
    <p class="para">Aliquam molestie, mi et imperdiet euismod, dui purus auctor tellus, et interdum lacus lectus et ante. Sed accumsan sollicitudin sapien, sit amet<br>adipiscing turpis gravida ac. In congue, neque ac lobortis volutpat, libero mauris varius mi, vitae suscipit ipsum ligula vitae risus. Duis aliquam<br>nibh a dui iaculis viverra id a velit. Vivamus egestas risus in magna varius commodo. Sed semper viverra egestas.<br>Etiam pretium porttitor lectus, vel ornare neque porta volutpat.</p>
    <span class="btn">Read More</span>
  </div>
</section>

<section class="offer">
  <div class="title"><div class="orn"></div><h2 class="heading">WHAT WE OFFER</h2></div>
  <svg class="abs arrow" style="left:20px" width="16" height="30" viewBox="0 0 16 30"><path d="M14 2 2 15l12 13" fill="none" stroke="#bbb" stroke-width="2"/></svg>
  <svg class="abs arrow" style="left:1164px" width="16" height="30" viewBox="0 0 16 30"><path d="M2 2l12 13L2 28" fill="none" stroke="#bbb" stroke-width="2"/></svg>
  <div class="card" style="left:75px">
    <div class="photo" role="img" aria-label="Dark blue image of a head with a glowing brain, representing the mind" style="background:radial-gradient(circle at 45% 50%,#2d4d78,#0c1628)"></div>
    <h3>MIND</h3>
    <p>Aliquam molestie, mi et imperdiet<br>euismod, dui purus auctor tellus,et interdum<br>lacus lectus.we denounce with righteous<br>indignation and dislike men<br>who are so beguiled</p>
  </div>
  <div class="card" style="left:434px">
    <div class="photo" role="img" aria-label="Silhouette of a person meditating against a green backdrop, representing the body" style="background:radial-gradient(circle at 50% 50%,#4f6e55,#1d2b22)"></div>
    <h3>BODY</h3>
    <p>Aliquam molestie, mi et imperdiet<br>euismod, dui purus auctor tellus,et interdum<br>lacus lectus.we denounce with righteous<br>indignation and dislike men<br>who are so beguiled</p>
  </div>
  <div class="card" style="left:793px">
    <div class="photo" role="img" aria-label="Calm grey sea under a cloudy sky, representing the spirit" style="background:linear-gradient(180deg,#3b4d5e,#7a8c98 55%,#2e3b45)"></div>
    <h3>SPIRIT</h3>
    <p>Aliquam molestie, mi et imperdiet<br>euismod, dui purus auctor tellus,et interdum<br>lacus lectus.we denounce with righteous<br>indignation and dislike men<br>who are so beguiled</p>
  </div>
</section>

<section class="temple">
  <div class="photo" role="img" aria-label="Ancient Greek temple ruins with columns under a blue sky" style="left:75px;top:54px;width:512px;height:307px;background:linear-gradient(180deg,#2f6fb8 0%,#8cb7e0 45%,#b89a6a 70%,#8a7552 100%)"></div>
  <div class="abs text">
    <div class="orn"></div>
    <h2 class="heading">GREEK TEMPLE</h2>
    <p class="para">Aliquam molestie, mi et imperdiet euismod, dui purus auctor tellus, et interdum lacus lectus et ante. Sed accumsan sollicitudin sapien, sit amet adipiscing turpis gravida ac. In congue, neque ac lobortis volutpat, libero mauris varius mi, vitae suscipit ipsum ligula vitae risus. Duis aliquam nibh a dui iaculis viverra id a velit.</p>
    <span class="btn">Read More</span>
  </div>
</section>

<section class="stories">
  <h2 class="abs sub" style="left:75px;top:44px">BLOG</h2>
  <h2 class="abs sub" style="left:614px;top:44px">TESTIMONIALS</h2>
  <article class="abs post" style="left:75px">
    <div class="photo" role="img" aria-label="Person meditating by the water at sunset" style="background:linear-gradient(180deg,#5b5f8a,#d98b4a 55%,#3a2a30)"></div>
    <h4>ALIQUAM MOLESTIE</h4>
    <p>Sed accumsan sollicitudin sapien, sit amet adipiscing turpis gravida neque ac lobortis..</p>
    <div class="date">Nov 19, 2016</div>
  </article>
  <article class="abs post" style="left:344px">
    <div class="photo" role="img" aria-label="Stone figure with a lotus flower among green leaves" style="background:linear-gradient(180deg,#8fbf4a,#4f7f2a 60%,#3a4a3a)"></div>
    <h4>ALIQUAM MOLESTIE</h4>
    <p>Sed accumsan sollicitudin sapien, sit amet adipiscing turpis gravida neque ac lobortis..</p>
    <div class="date">Nov 19, 2016</div>
  </article>
  <div class="abs quote-box">
    <span class="abs qmark" style="left:14px;top:6px">“</span>
    <p>“ Aliquam molestie, mi et imperdiet euismod, dui purus auctor tellus, et interdum lacus lectus et ante. Sed accumsan sollicitudin sapien, sit amet adipiscing turpis gravida ac. In congue, neque ac lobortis volutpat, libero mauris varius...”</p>
    <div class="who">-Name Heading</div>
    <span class="abs qmark" style="right:16px;top:140px">”</span>
  </div>
  <div class="abs avatar" role="img" aria-label="Portrait of the client giving the testimonial"></div>
  <div class="abs dots"><i></i><i></i><i></i><i></i></div>
</section>

<section class="newsletter">
  <div class="inner">
    <div class="orn"></div>
    <h2 class="heading">SIGN UP NEWSLETTER</h2>
    <p class="para">Aliquam molestie, mi et imperdiet euismod, dui purus auctor tellus, et interdum lacus lectus et ante.</p>
    <div class="signup">
      <div class="field">Enter Email Address</div>
      <span class="btn">Subscribe</span>
    </div>
  </div>
</section>

<footer class="site-footer">
  <nav class="abs footnav">
    <span>Home</span><span>About Us</span><span>Services</span><span>Blog</span><span>Testimonials</span><span>News</span><span>Contact Us</span>
  </nav>
  <div class="abs legal">Copyright © 2016. Lantern of the Meadow. All Right Reserved<br>Privacy Policy | Terms &amp; Conditions</div>
  <div class="abs follow">Follow Us</div>
  <div class="abs socials"><i></i><i></i><i></i><i></i><i></i></div>
</footer>

</body>
</html>
```